Cybersecurity Start-Up - Veloriq

We need a MS Word Template for everyday documents. This would be leveraged to create reports, marketing materials, internal memos etc.

The document should follow the standard MS Word template format and have an H1,H2,H3, paragraph, Title, bold font, regular font, table etc. All editable with normal MS Word features.

Our logo is also attached. We would like to see the same color scheme used throughout the document. Additional attached is a sample word document that outlines all of the components we would like to see in the template.

Requirements
Must have
• - Submission must meet all standard MS Word Template requirements.
• - Submission should make use of Built in MS Styles so as the user of the template I should be able to create a brand new page and insert an H1 for example and be able to select from the styles drop down the same font/color/style that you have designed for your submission.
• - All sections in the provided document need to be contained in your submission.
• - The table of contents should auto update if I add a new page, heading, section etc.
• - Need to read and understand all of my comments which I have placed in the sample document uploaded to the briefing
Should not have
• no fixed textboxes or image boxes. everything needs to be smoothly editable in MS Word. "Editable" means more than just being able to alter text.

```html
<!DOCTYPE html>
<html lang="en">
<head>
<meta charset="utf-8">
<title>Veloriq Document Template</title>
<link href="https://fonts.googleapis.com/css2?family=Open+Sans:wght@300;400;600;700&display=swap" rel="stylesheet">
<style>
:root{
  --dark-green:#0e6b45;
  --light-green:#52c07f;
  --ink:#1c1c1c;
  --muted:#3a3a3a;
  --canvas:#ebebeb;
  --page:#ffffff;
  --soft-grey:#ececec;
  --row-grey:#eeeeee;
  --label:#2b3440;
  --cyber-deep:#020a3a;
  --cyber-bright:#1f7cf0;
}
*{box-sizing:border-box;margin:0;padding:0}
html,body{width:883px;height:1200px;overflow:hidden}
body{background:var(--canvas);font-family:"Open Sans",Arial,sans-serif;color:var(--ink);position:relative}

.page{position:absolute;width:359px;height:508px;background:var(--page);box-shadow:0 1px 4px rgba(0,0,0,.25);overflow:hidden}
.cover-one{left:54px;top:22px}
.cover-two{left:468px;top:22px;background:var(--soft-grey)}
.contents-page{left:54px;top:612px}
.intro-page{left:468px;top:612px}

.sheet-label{position:absolute;width:359px;text-align:center;font-size:24px;font-weight:400;color:var(--label);letter-spacing:.5px}

.abs{position:absolute}

/* footer band */
.page-footer{position:absolute;left:0;right:0;top:480px;height:19px;background:var(--dark-green);color:#fff;font-size:7.5px;font-weight:600}
.page-footer .date{position:absolute;left:17px;top:4px;word-spacing:3px}
.page-footer .web{position:absolute;left:130px;top:4px;letter-spacing:1.6px}
.page-footer .num{position:absolute;right:16px;top:4px}

/* wordmark */
.wordmark{display:flex;align-items:center;gap:5px}
.wordmark .dot{width:11px;height:11px;border-radius:50%;background:currentColor}
.wordmark .name{font-weight:700;letter-spacing:.5px}

/* cover one */
.cover-one .title-top{left:16px;top:30px;font-size:30px;font-weight:400;line-height:1;color:var(--ink)}
.cover-one .title-green{left:17px;top:60px;font-size:27px;font-weight:600;line-height:1;color:var(--light-green)}
.cyber-art{background:radial-gradient(ellipse at 55% 50%,var(--cyber-bright) 0%,#0a3fb0 35%,var(--cyber-deep) 80%)}
.cover-one .cyber-art{left:0;top:122px;width:359px;height:284px}
.cover-one .logo-box{left:204px;top:99px;width:123px;height:48px;background:var(--dark-green);border:2px solid #fff;color:#fff;justify-content:center;font-size:17px}
.cover-one .subtitle-a{left:0;width:359px;top:418px;text-align:center;font-size:24px;font-weight:400}
.cover-one .subtitle-b{left:0;width:359px;top:450px;text-align:center;font-size:16px;font-weight:700;letter-spacing:6.5px}

/* cover two */
.cover-two .shapes{position:absolute;left:0;top:0}
.cover-two .logo-light{left:18px;top:236px;color:#fff;font-size:17px}
.cover-two .cover-title{left:16px;top:402px;font-size:21px;font-weight:300;color:var(--ink);letter-spacing:.3px}
.cover-two .cover-strap{left:0;top:434px;width:304px;height:15px;background:var(--dark-green);color:#fff;font-size:10px;letter-spacing:1.8px;padding-left:18px;line-height:15px}

/* inner pages */
.header-rule{position:absolute;top:26px;height:1.5px;background:var(--dark-green)}
.header-logo{position:absolute;top:13px;right:16px;color:var(--dark-green);font-size:12px}
.header-logo .dot{width:10px;height:10px}
.header-web{position:absolute;top:28px;right:16px;font-size:4.5px;color:var(--light-green);letter-spacing:.5px}

.tag{position:absolute;left:0;height:16px;line-height:16px;color:#fff;font-size:11.5px;padding-left:17px}
.tag.green{background:var(--dark-green)}
.tag.black{background:#000}

.toc{position:absolute;left:25px;top:106px;width:315px;list-style:none}
.toc li{position:relative;height:24.2px;font-size:7.5px;color:var(--muted)}
.toc .leader{position:absolute;left:173px;width:110px;top:7px;border-bottom:1px dotted #555}
.toc .pg{position:absolute;left:306px}

.section-heading{position:absolute;left:0;right:0;top:60px;display:flex;align-items:center;gap:6px;color:var(--dark-green);font-weight:700;font-size:12.5px}
.section-heading::before,.section-heading::after{content:"";height:1.5px;background:var(--dark-green);flex:1}
.section-heading::before{flex:0 0 105px}
.section-heading::after{flex:1}

.body-copy{position:absolute;left:17px;width:326px;font-size:7.2px;line-height:12px;color:var(--muted);text-align:justify}

.roles-table{position:absolute;left:18px;top:261px;width:325px;border:1px solid #ddd;border-collapse:collapse;font-size:6.5px;color:var(--muted)}
.roles-table th{background:var(--light-green);color:#fff;text-align:left;font-weight:600;height:16px;padding-left:10px;font-size:7px}
.roles-table td{padding:0 0 0 10px;height:17.5px;vertical-align:middle}
.roles-table tr.alt td{background:var(--row-grey)}
.roles-table tr.tall td{height:35px;vertical-align:top;padding-top:6px;line-height:12px}
.roles-table td.value{width:134px;padding-left:0}
</style>
</head>
<body>

<!-- Cover 01 -->
<section class="page cover-one">
  <h1 class="abs title-top">CELTIBERIAN</h1>
  <p class="abs title-green">WARS (130 BC)</p>
  <div class="abs cyber-art" role="img" aria-label="Blue cyber security word cloud with binary code streams and a pointing hand cursor"></div>
  <div class="abs logo-box wordmark"><span class="dot"></span><span class="name">VELORIQ</span></div>
  <p class="abs subtitle-a">AN ANCIENT CELTIBERIAN</p>
  <p class="abs subtitle-b">SETTLEMENT IN SPAIN</p>
  <footer class="page-footer"><span class="date">Month, Day, Year</span><span class="web">www.veloriq.com</span><span class="num">01</span></footer>
</section>
<div class="sheet-label" style="left:54px;top:556px">COVER - 01</div>

<!-- Cover 02 -->
<section class="page cover-two">
  <svg class="shapes" width="359" height="508" viewBox="0 0 449 635">
    <defs>
      <radialGradient id="cyberGlow" cx="55%" cy="40%" r="65%">
        <stop offset="0" stop-color="#1f7cf0"/>
        <stop offset=".4" stop-color="#0a3fb0"/>
        <stop offset="1" stop-color="#020a3a"/>
      </radialGradient>
      <clipPath id="stripeClip"><polygon points="449,165 449,345 362,255"/></clipPath>
    </defs>
    <polygon points="0,0 449,0 449,160 258,352 190,318 0,110" fill="url(#cyberGlow)" role="img" aria-label="Blue cyber security word cloud with a pointing hand cursor"/>
    <polygon points="0,135 185,318 0,500" fill="#0e6b45"/>
    <polygon points="190,327 190,437 80,437" fill="#52c07f"/>
    <polygon points="262,357 355,270 445,360 355,452" fill="#52c07f"/>
    <polygon points="449,372 449,548 362,460" fill="#0e6b45"/>
    <g clip-path="url(#stripeClip)" stroke="#0e6b45" stroke-width="3">
      <line x1="366" y1="160" x2="366" y2="350"/><line x1="374" y1="160" x2="374" y2="350"/>
      <line x1="382" y1="160" x2="382" y2="350"/><line x1="390" y1="160" x2="390" y2="350"/>
      <line x1="398" y1="160" x2="398" y2="350"/><line x1="406" y1="160" x2="406" y2="350"/>
      <line x1="414" y1="160" x2="414" y2="350"/><line x1="422" y1="160" x2="422" y2="350"/>
      <line x1="430" y1="160" x2="430" y2="350"/><line x1="438" y1="160" x2="438" y2="350"/>
      <line x1="446" y1="160" x2="446" y2="350"/>
    </g>
  </svg>
  <div class="abs logo-light wordmark"><span class="dot"></span><span class="name">VELORIQ</span></div>
  <h1 class="abs cover-title">CELTIBERIAN WARS (130 BC)</h1>
  <p class="abs cover-strap">An ancient Celtiberian settlement in Spain</p>
  <footer class="page-footer"><span class="date">Month, Day, Year</span><span class="web">www.veloriq.com</span><span class="num">01</span></footer>
</section>
<div class="sheet-label" style="left:468px;top:556px">COVER - 02</div>

<!-- Page 02 -->
<section class="page contents-page">
  <div class="header-rule" style="left:0;width:266px"></div>
  <div class="header-logo wordmark"><span class="dot"></span><span class="name">VELORIQ</span></div>
  <div class="header-web">www.veloriq.com</div>
  <h2 class="tag green" style="top:70px;width:117px;font-weight:400">Table of Contents</h2>
  <ol class="toc">
    <li>Training Name<span class="leader"></span><span class="pg">1</span></li>
    <li>Subject Introduction<span class="leader"></span><span class="pg">3</span></li>
    <li>Subjects recommended<span class="leader"></span><span class="pg">3</span></li>
    <li>Professional Outcomes<span class="leader"></span><span class="pg">3</span></li>
    <li>Training Content<span class="leader"></span><span class="pg">3</span></li>
    <li>Technical Overview<span class="leader"></span><span class="pg">4</span></li>
    <li>Severity Ratings<span class="leader"></span><span class="pg">4</span></li>
    <li>Summary Of Findings<span class="leader"></span><span class="pg">4</span></li>
    <li>Detailed Observations<span class="leader"></span><span class="pg">5</span></li>
    <li>Critical Findings<span class="leader"></span><span class="pg">5</span></li>
    <li>High Findings<span class="leader"></span><span class="pg">5</span></li>
    <li>Medium Findings<span class="leader"></span><span class="pg">5</span></li>
    <li>Low Findings<span class="leader"></span><span class="pg">5</span></li>
    <li>Appendix 01 – Engagement Methodology<span class="leader"></span><span class="pg">6</span></li>
  </ol>
  <footer class="page-footer"><span class="date">Month, Day, Year</span><span class="web">www.veloriq.com</span><span class="num">02</span></footer>
</section>
<div class="sheet-label" style="left:54px;top:1148px">PAGE - 02</div>

<!-- Page 03 -->
<section class="page intro-page">
  <div class="header-rule" style="left:0;width:266px"></div>
  <div class="header-logo wordmark"><span class="dot"></span><span class="name">VELORIQ</span></div>
  <div class="header-web">www.veloriq.com</div>
  <h2 class="section-heading">SUBJECT INTRODUCTION</h2>
  <p class="body-copy" style="top:84px">Lorem Ipsum is simply dummy text of the printing and typesetting industry. Lorem Ipsum has been the industry's standard dummy text ever since the 1500s, when an unknown printer took a galley of type and scrambled it to make a type specimen book.</p>
  <h3 class="tag black" style="top:145px;width:147px;font-weight:400">Subjects recommended</h3>
  <p class="body-copy" style="top:172px">Lorem Ipsum is simply dummy text of the printing and typesetting industry. Lorem Ipsum has been the industry's standard dummy text ever since the 1500s, when an unknown printer took a galley of type and scrambled it to make a type specimen book.</p>
  <h3 class="tag black" style="top:231px;width:144px;font-weight:400">Professional Outcomes</h3>
  <table class="roles-table">
    <tr><th colspan="2">WORK ROLES – TABLE 1</th></tr>
    <tr><td colspan="2">Work Roles Name</td></tr>
    <tr class="alt"><td colspan="2">Specialty Area</td></tr>
    <tr><td colspan="2">CSF Category</td></tr>
    <tr class="alt"><td colspan="2">Work Role Description</td></tr>
    <tr class="tall"><td>Tasks</td><td class="value">This is task 1<br>This is task 2</td></tr>
    <tr class="tall alt"><td>Skills</td><td class="value">This is skill 1<br>This is skill 2</td></tr>
    <tr class="tall"><td>Abilities</td><td class="value">This is ability 1<br>This is ability 2</td></tr>
  </table>
  <footer class="page-footer"><span class="date">Month, Day, Year</span><span class="web">www.veloriq.com</span><span class="num">03</span></footer>
</section>
<div class="sheet-label" style="left:468px;top:1148px">PAGE - 03</div>

</body>
</html>
```